Whitmore Business Card Design

The name of the business is Dara Whitmore, CPA LLC
The service that we offer is Accounting, Tax & Consulting Services. I need it to have the following items:
Dara Whitmore, Principal
Phone Number
Email Address
Physical Address

I have attached the company logo, one in black and one in white. Please provide a design in black background and the other in white background. Please include "Accounting, Tax & Consulting Services". I want the business card to be clean and very professional.

```html
<!DOCTYPE html>
<html lang="en">
<head>
<meta charset="utf-8">
<title>Dara Whitmore, CPA LLC — Business Card</title>
<link rel="stylesheet" href="https://fonts.googleapis.com/css2?family=Montserrat:wght@400;500;600;700&family=Bebas+Neue&display=swap">
<style>
  :root {
    --canvas: #d3d4d6;
    --card-light: #ffffff;
    --card-dark: #3b3b3d;
    --ink: #3a3a3c;
    --ink-soft: #6d6e71;
    --brand-red: #9b1b1e;
    --white: #ffffff;
  }
  * { margin: 0; padding: 0; box-sizing: border-box; }
  html, body {
    width: 1015px; height: 1200px; overflow: hidden;
    background: var(--canvas);
    font-family: "Montserrat", sans-serif;
  }
  .card {
    position: absolute; left: 82px; width: 822px; height: 470px;
    border-radius: 36px; overflow: hidden;
    box-shadow: 0 8px 24px rgba(0,0,0,0.22);
  }
  .card--front { top: 82px; background: var(--card-light); color: var(--ink); }
  .card--back { top: 600px; background: var(--card-dark); color: var(--white); }

  .abs { position: absolute; white-space: nowrap; }

  .firm-name { left: 45px; top: 148px; font-size: 23px; font-weight: 600; color: var(--ink); letter-spacing: 0.2px; }
  .firm-tagline { left: 46px; top: 178px; font-size: 15.5px; font-weight: 500; color: var(--ink-soft); letter-spacing: 2px; }

  .person-name { left: 39px; top: 232px; font-size: 38px; font-weight: 700; color: var(--brand-red); letter-spacing: -1px; }
  .person-title { left: 40px; top: 280px; font-size: 22px; font-weight: 400; color: var(--ink); }
  .divider { left: 41px; top: 319px; width: 728px; height: 1.5px; background: var(--ink); }

  .contact { left: 40px; display: flex; align-items: center; gap: 22px; font-size: 22px; color: var(--ink); }
  .contact svg { width: 20px; height: 20px; fill: var(--brand-red); flex: none; }
  .contact--phone { top: 333px; }
  .contact--email { top: 364px; }
  .contact--web { top: 398px; }

  .address { left: 534px; top: 361px; font-size: 22px; line-height: 32px; color: var(--ink); }

  .band { left: 0; top: 0; width: 822px; height: 470px; }
  .services {
    right: 24px; top: 439px; height: 28px; line-height: 28px;
    font-family: "Bebas Neue", sans-serif;
    font-size: 28px; color: var(--white); letter-spacing: 0.2px;
    transform: scaleX(0.78); transform-origin: right center;
  }

  .back-name { left: 0; width: 822px; text-align: center; top: 264px; font-size: 35.5px; font-weight: 600; color: var(--white); }
  .back-tagline { left: 0; width: 822px; text-align: center; top: 311px; font-size: 25px; font-weight: 600; color: var(--white); letter-spacing: 3px; }
</style>
</head>
<body>
  <section class="card card--front" aria-label="Business card front">
    <p class="abs firm-name">DARA WHITMORE, CPA, LLC</p>
    <p class="abs firm-tagline">CERTIFIED PUBLIC ACCOUNTANT</p>

    <h1 class="abs person-name">DARA WHITMORE</h1>
    <p class="abs person-title">Principal</p>
    <div class="abs divider"></div>

    <p class="abs contact contact--phone">
      <svg viewBox="0 0 24 24" aria-hidden="true"><path d="M6.6 10.8c1.4 2.8 3.8 5.2 6.6 6.6l2.2-2.2c.3-.3.7-.4 1-.2 1.1.4 2.3.6 3.6.6.6 0 1 .4 1 1V20c0 .6-.4 1-1 1C10.6 21 3 13.4 3 4c0-.6.4-1 1-1h3.5c.6 0 1 .4 1 1 0 1.3.2 2.5.6 3.6.1.3 0 .7-.2 1z"/></svg>
      044-555 210 734
    </p>
    <p class="abs contact contact--email">
      <svg viewBox="0 0 24 24" aria-hidden="true"><path d="M2 5h20v14H2z"/><path d="M3 6l9 7 9-7" stroke="#fff" stroke-width="1.4" fill="none"/></svg>
      info@whitmorecpa.com
    </p>
    <p class="abs contact contact--web">
      <svg viewBox="0 0 24 24" aria-hidden="true"><circle cx="12" cy="12" r="10"/><path d="M7 7c2 1 3 3 2 5s1 3 1 5M14 4c0 2 2 3 3 3s2 2 1 4-2 2-2 4" stroke="#fff" stroke-width="1.3" fill="none"/></svg>
      www.whitmorecpa.com
    </p>

    <p class="abs address">421, Address line here<br>Country Name, 45452</p>

    <svg class="abs band" viewBox="0 0 822 470" aria-hidden="true">
      <polygon points="0,446 474,446 462,458 0,458" fill="var(--brand-red)"/>
      <rect x="0" y="459" width="822" height="11" fill="var(--ink)"/>
      <polygon points="458,470 494,436 822,436 822,470" fill="var(--ink)"/>
    </svg>
    <p class="abs services">ACCOUNTING, TAX &amp; CONSULTING SERVICES</p>
  </section>

  <section class="card card--back" aria-label="Business card back">
    <p class="abs back-name">DARA WHITMORE, CPA, LLC</p>
    <p class="abs back-tagline">CERTIFIED PUBLIC ACCOUNTANT</p>
  </section>
</body>
</html>
```